FLYER FÜR VITALQUELL HAMBURG
Zielgruppe
Zielgruppe ist zwischen 30 und 45 Jahre alt und berufstätig. Mit wenig Zeit für Einkauf und Zubereitung von Speisen, aber sehr gesundheitsbewusst und sportlich.
Aufgabenstellung
Ich bräuchte einen schnellen Flyer für Vitalquell-Hamburg.com. Das Design sollte dem der Website entsprechen.
Ich habe auch eine Vorlage, die genommen werden kann, aber nicht muss.
Fotos und Texte liefere ich.
Der Flyer sollte Din hoch sein und zum aufklappen.
Ansonsten bin ich flexibel, sollte halt schön sein.
Preis inkl. MwSt, ich benötige eine Rechnung.

```html
<!DOCTYPE html>
<html lang="de">
<head>
<meta charset="utf-8">
<title>Flyer Vitalquell Hamburg – Layout</title>
<link rel="stylesheet" href="https://fonts.googleapis.com/css2?family=Oswald:wght@400;500;700&family=Roboto+Condensed:wght@400&display=swap">
<style>
  :root {
    --brand-green: #3aa846;
    --band-green: #5cb866;
    --white: #ffffff;
    --label-ink: #111111;
    --paper: #ffffff;
    --divider: rgba(255,255,255,0.85);
  }
  * { margin: 0; padding: 0; box-sizing: border-box; }
  html, body { width: 1200px; height: 900px; overflow: hidden; background: var(--paper); }
  .sheet { position: relative; width: 1200px; height: 900px; font-family: "Oswald", sans-serif; }

  .side-label { position: absolute; top: 68px; font-family: "Roboto Condensed", sans-serif; font-size: 14px; color: var(--label-ink); }
  .side-label--back { left: 104px; }
  .side-label--front { left: 600px; }

  .spread { position: absolute; left: 104px; width: 992px; height: 248px; background: var(--brand-green); overflow: hidden; }
  .spread--outside { top: 98px; }
  .spread--inside { top: 438px; }
  .spread__fold { position: absolute; top: 0; left: 495px; width: 1px; height: 100%; background: var(--divider); }

  .leaf-band { position: absolute; left: 0; bottom: 0; height: 32px; background: linear-gradient(180deg, var(--brand-green), var(--band-green)); }

  .brand-name { position: absolute; color: var(--white); font-weight: 700; font-size: 38px; line-height: 0.92; letter-spacing: 0.5px; text-transform: uppercase; }
  .brand-name span { display: block; }
  .brand-name--back { left: 30px; top: 32px; }
  .brand-name--front { left: 525px; top: 32px; }

  .contact { position: absolute; left: 348px; top: 30px; font-family: "Roboto Condensed", sans-serif; font-style: normal; font-size: 9.5px; line-height: 11.6px; color: var(--white); text-transform: uppercase; }

  .photo { position: absolute; }
  .photo--juices { left: 760px; top: 31px; width: 232px; height: 169px; background: linear-gradient(90deg, #f1e6dc 0%, #f3a55a 22%, #ea8c4c 38%, #ede4e6 55%, #d4dba6 72%, #f2cf8e 90%, #efe7df 100%); }
  .photo--dish { left: 0; top: 0; width: 497px; height: 248px; background: radial-gradient(ellipse at 55% 55%, #6d8a3e 0%, #a44a34 35%, #e9e3dc 62%, #c6563f 100%); }

  .claim { position: absolute; left: 526px; top: 182px; font-size: 17px; font-weight: 400; color: var(--white); letter-spacing: 0.3px; }

  .headline { position: absolute; left: 72px; top: 132px; font-size: 18px; font-weight: 700; color: var(--white); text-transform: uppercase; letter-spacing: 0.2px; }

  .teaser { position: absolute; display: flex; align-items: flex-start; gap: 4px; }
  .teaser__thumb { flex: 0 0 97px; width: 97px; height: 82px; background: linear-gradient(135deg, #b6352a 0%, #8f6a3e 45%, #c9a06a 70%, #b8c67a 100%); }
  .teaser__text { width: 112px; color: var(--white); }
  .teaser__title { font-size: 12px; font-weight: 500; line-height: 13px; text-transform: uppercase; white-space: nowrap; }
  .teaser__body { font-family: "Roboto Condensed", sans-serif; font-size: 7.8px; line-height: 9.2px; margin-top: 4px; }

  .teaser--a { left: 528px; top: 31px; }
  .teaser--b { left: 748px; top: 31px; }
  .teaser--c { left: 528px; top: 136px; }
  .teaser--d { left: 748px; top: 136px; }
</style>
</head>
<body>
<main class="sheet">
  <p class="side-label side-label--back">Rückseite</p>
  <p class="side-label side-label--front">Vorderseite</p>

  <section class="spread spread--outside">
    <h2 class="brand-name brand-name--back"><span>Vitalquell</span><span>Hamburg</span></h2>
    <address class="contact">
      Vitalquell Food Delivery<br>
      Lindenstieg 14<br>
      20146 Hamburg<br>
      Tel 040 00 12 34 56<br>
      Fax 040 00 98 76 54<br>
      www.vitalquell-hamburg.com<br>
      info@vitalquell-hamburg.com
    </address>
    <div class="leaf-band" style="width:495px" role="img" aria-label="Dezente Reihe aus Kräuterblättern am unteren Rand"></div>

    <div class="spread__fold"></div>

    <h1 class="brand-name brand-name--front"><span>Vitalquell</span><span>Hamburg</span></h1>
    <div class="photo photo--juices" role="img" aria-label="Foto: Glasflaschen mit bunten frischen Säften"></div>
    <p class="claim">„MAN IST, WAS MAN ISST.“</p>
    <div class="leaf-band" style="left:496px;width:496px" role="img" aria-label="Dezente Reihe aus Kräuterblättern am unteren Rand"></div>
  </section>

  <section class="spread spread--inside">
    <div class="photo photo--dish" role="img" aria-label="Foto: Teller mit gegrilltem Thunfisch, Spargel und Tomatensalat"></div>
    <h2 class="headline">Das ist eine Headline, sowieso anders.</h2>

    <div class="leaf-band" style="left:496px;width:496px" role="img" aria-label="Dezente Reihe aus Kräuterblättern am unteren Rand"></div>

    <div class="spread__fold"></div>

    <article class="teaser teaser--a">
      <div class="teaser__thumb" role="img" aria-label="Foto: frische Zutaten und Gemüse"></div>
      <div class="teaser__text">
        <h3 class="teaser__title">Das ist eine Subhead.</h3>
        <p class="teaser__body">Lorem ipsum dolor sit amet, consetetur sadipscing elitr, sed diam nonumy eirmod tempor invidunt ut labore et dolore magna aliquyam erat, sed diam voluptua. At vero eos et accusam et justo duo dolores et ea rebum. Stet clita kasd gubergren, no sea</p>
      </div>
    </article>
    <article class="teaser teaser--b">
      <div class="teaser__thumb" role="img" aria-label="Foto: frische Zutaten und Gemüse"></div>
      <div class="teaser__text">
        <h3 class="teaser__title">Das ist eine Subhead.</h3>
        <p class="teaser__body">Lorem ipsum dolor sit amet, consetetur sadipscing elitr, sed diam nonumy eirmod tempor invidunt ut labore et dolore magna aliquyam erat, sed diam voluptua. At vero eos et accusam et justo duo dolores et ea rebum. Stet clita kasd gubergren, no sea</p>
      </div>
    </article>
    <article class="teaser teaser--c">
      <div class="teaser__thumb" role="img" aria-label="Foto: frische Zutaten und Gemüse"></div>
      <div class="teaser__text">
        <h3 class="teaser__title">Das ist eine Subhead.</h3>
        <p class="teaser__body">Lorem ipsum dolor sit amet, consetetur sadipscing elitr, sed diam nonumy eirmod tempor invidunt ut labore et dolore magna aliquyam erat, sed diam voluptua. At vero eos et accusam et justo duo dolores et ea rebum. Stet clita kasd gubergren, no sea</p>
      </div>
    </article>
    <article class="teaser teaser--d">
      <div class="teaser__thumb" role="img" aria-label="Foto: frische Zutaten und Gemüse"></div>
      <div class="teaser__text">
        <h3 class="teaser__title">Das ist eine Subhead.</h3>
        <p class="teaser__body">Lorem ipsum dolor sit amet, consetetur sadipscing elitr, sed diam nonumy eirmod tempor invidunt ut labore et dolore magna aliquyam erat, sed diam voluptua. At vero eos et accusam et justo duo dolores et ea rebum. Stet clita kasd gubergren, no sea</p>
      </div>
    </article>
  </section>
</main>
</body>
</html>
```